Stationary Design for Consulting company
The Lumora Collective
Stationary Design for Consulting company  - Consulting
Creative Brief
Professional
Marlene Vostrikova
Founder & Managing Director
Zarin Plaza Faris Road P.O. Box 246813 Abu Dhabi United Arab Emirates
marlene@thelumoracollective.example
www.thelumoracollective.example
Stationary design should be innovative, sleek, professional, color binds to white, blue and gray as in logo
back side of business card needs to be in arabic
BettyLou BettyLou
@All please stay away from too much blue .. i want a sleek white, light grey design and minimal color
#74-76 I like the watermark K though ..keep it :)
#76 try to be more creative when it comes to the placement of the company logo ... i want to stay away from the mainstream upper left, center and right :)

```html
<!DOCTYPE html>
<html lang="en">
<head>
<meta charset="utf-8">
<title>The Lumora Collective — Stationery</title>
<link rel="stylesheet" href="https://fonts.googleapis.com/css2?family=Open+Sans:wght@400;600&family=Great+Vibes&display=swap">
<style>
  :root {
    --bg: #e9eaec;
    --paper: #ffffff;
    --ink: #3d4249;
    --muted: #8a9099;
    --rule: #d5d8dc;
    --accent: #2f7fb8;
    --watermark: #eef2f6;
    --dark: #2b2d31;
    --dark-edge: #1e2023;
    --on-dark: #e8ebee;
  }
  * { box-sizing: border-box; margin: 0; padding: 0; }
  html, body { width: 1200px; height: 763px; overflow: hidden; }
  body {
    position: relative;
    background: var(--bg);
    font-family: "Open Sans", Arial, sans-serif;
    color: var(--ink);
  }
  .sheet { position: absolute; background: var(--paper); box-shadow: 0 1px 3px rgba(0,0,0,.12); }
  .brand { font-family: "Open Sans", Arial, sans-serif; font-weight: 600; color: var(--accent); white-space: nowrap; }
  .brand-on-dark { color: var(--on-dark); }

  /* business cards */
  .card-front { left: 156px; top: 132px; width: 150px; height: 84px; background: var(--dark);
    display: flex; align-items: center; padding-left: 16px; }
  .card-front .brand { font-size: 10px; }
  .card-back { left: 336px; top: 132px; width: 151px; height: 84px; padding: 12px 14px; }
  .card-back .brand { font-size: 9px; }
  .card-back .person { margin-top: 7px; font-size: 5.5px; font-weight: 600; }
  .card-back .role { font-size: 4.5px; color: var(--muted); }
  .card-back .contact { margin-top: 4px; font-size: 4px; line-height: 1.4; color: var(--muted); }

  /* envelope */
  .envelope { left: 125px; top: 240px; width: 362px; height: 182px; padding: 18px 20px; overflow: hidden; }
  .envelope .brand { font-size: 11px; }
  .envelope .return { margin-top: 6px; font-size: 5px; line-height: 1.5; color: var(--muted); }
  .envelope .watermark { position: absolute; left: 50px; bottom: 0; width: 150px; height: 90px;
    background: radial-gradient(ellipse at 50% 70%, var(--watermark) 0%, rgba(238,242,246,0) 70%); }

  /* letterhead */
  .letterhead { left: 512px; top: 128px; width: 357px; height: 506px; padding: 24px 36px 0 36px; }
  .letterhead .brand { font-size: 15px; }
  .letterhead .edge-rule { position: absolute; left: 22px; top: 70px; width: 1px; height: 360px; background: var(--rule); }
  .letter-body { margin-top: 56px; font-size: 6.2px; line-height: 1.8; color: var(--ink); }
  .letter-body p { margin-bottom: 10px; }
  .signature { margin-top: 18px; }
  .signature .script { font-family: "Great Vibes", cursive; font-size: 20px; color: var(--ink); }
  .signature .title { font-size: 5.5px; color: var(--muted); }
  .letter-footer { position: absolute; left: 36px; right: 36px; bottom: 18px; border-top: 1px solid var(--rule);
    padding-top: 6px; display: flex; justify-content: space-between; font-size: 4.5px; line-height: 1.5; color: var(--muted); }

  /* notebook */
  .notebook { left: 895px; top: 125px; width: 183px; height: 260px; background: var(--dark);
    border-left: 6px solid var(--dark-edge); padding: 34px 20px; }
  .notebook .brand { font-size: 12px; }
  .notebook .binding { position: absolute; right: -4px; top: 6px; }
</style>
</head>
<body>

  <section class="sheet card-front" aria-label="Business card front">
    <span class="brand brand-on-dark">The Lumora Collective</span>
  </section>

  <section class="sheet card-back" aria-label="Business card back">
    <div class="brand">The Lumora Collective</div>
    <div class="person">Marlene Vostrikova</div>
    <div class="role">Founder &amp; Managing Director</div>
    <div class="contact">
      +971 2 555 0148<br>
      marlene@thelumoracollective.example<br>
      www.thelumoracollective.example
    </div>
  </section>

  <section class="sheet envelope" aria-label="Envelope">
    <div class="watermark" role="img" aria-label="Faint brand watermark"></div>
    <div class="brand">The Lumora Collective</div>
    <div class="return">Zarin Plaza Faris Road P.O. Box 246813<br>Abu Dhabi, United Arab Emirates</div>
  </section>

  <section class="sheet letterhead" aria-label="Letterhead">
    <div class="edge-rule"></div>
    <div class="brand">The Lumora Collective</div>
    <div class="letter-body">
      <p>Dear Reader,</p>
      <p>Thank you for your time and interest in our work. We help teams grow through clear goals, steady coaching and practical tools that fit the way they already work every day.</p>
      <p>Our consultants listen first, then shape programs around your people. Each plan is reviewed with you so that progress can be measured and shared openly.</p>
      <p>From early planning to final review, we stay close to your leaders and staff. Regular check-ins keep every project on track and every voice heard.</p>
      <p>Our approach is simple and calm. We focus on small daily improvements that add up to lasting change across the whole organisation.</p>
      <p>We look forward to meeting with you and your team to discuss the next steps. Please feel free to contact us at any time with questions.</p>
      <p>Kind regards,</p>
    </div>
    <div class="signature">
      <div class="script">Your Name</div>
      <div class="title">Company Director</div>
    </div>
    <footer class="letter-footer">
      <span>+971 2 555 0148<br>Zarin Plaza Faris Road P.O. Box 246813</span>
      <span>marlene@thelumoracollective.example<br>www.thelumoracollective.example</span>
    </footer>
  </section>

  <section class="sheet notebook" aria-label="Notebook cover">
    <div class="brand brand-on-dark">The Lumora Collective</div>
    <svg class="binding" width="8" height="248" viewBox="0 0 8 248" aria-hidden="true">
      <g fill="none" stroke="#5a5e64" stroke-width="1.5">
        <circle cx="4" cy="6" r="3"/><circle cx="4" cy="18" r="3"/><circle cx="4" cy="30" r="3"/>
        <circle cx="4" cy="42" r="3"/><circle cx="4" cy="54" r="3"/><circle cx="4" cy="66" r="3"/>
        <circle cx="4" cy="78" r="3"/><circle cx="4" cy="90" r="3"/><circle cx="4" cy="102" r="3"/>
        <circle cx="4" cy="114" r="3"/><circle cx="4" cy="126" r="3"/><circle cx="4" cy="138" r="3"/>
        <circle cx="4" cy="150" r="3"/><circle cx="4" cy="162" r="3"/><circle cx="4" cy="174" r="3"/>
        <circle cx="4" cy="186" r="3"/><circle cx="4" cy="198" r="3"/><circle cx="4" cy="210" r="3"/>
        <circle cx="4" cy="222" r="3"/><circle cx="4" cy="234" r="3"/>
      </g>
    </svg>
  </section>

</body>
</html>
```